High Tech Real Estate Startup needs a business card

We are developing an innovative real estate marketing product based around advanced search and virtual reality.

We talk to people, we need business cards.

Target Market(s)

The target market is technology professionals and realtors.

Contact Information for Business Card

The information to be included will include

Name
Title
Phone Number
E-mail Address
www.plindo.com

It should use simple iconography for each one of those fields.

Font styles to use
Other font styles liked:
• Co, Jubilat, Avenir

Colors

Designer to choose colors to be used in the design.

Requirements
Must have
• Clean aesthetic,
• Good use of negative space.
• It should use our company logo, shown in the attached file. It is able to use the negative of that logo (coloured font and white background) and I have attached other acceptable accent colours in a swatch file.
Should not have
• Should not be too busy
• No extraneous text (slogans, tag lines etc)

```html
<!DOCTYPE html>
<html lang="en">
<head>
<meta charset="utf-8">
<title>Plindo Business Cards</title>
<link rel="stylesheet" href="https://fonts.googleapis.com/css2?family=Roboto:wght@400;500&family=Roboto+Condensed:wght@700&display=swap">
<style>
  :root {
    --teal: #00b0b6;
    --charcoal: #393939;
    --paper: #f5f5f5;
    --backdrop: #ebebeb;
    --ink: #3a3a3a;
    --white: #ffffff;
  }
  * { box-sizing: border-box; margin: 0; padding: 0; }
  html, body {
    width: 1200px; height: 800px; overflow: hidden;
    background: var(--backdrop);
    font-family: "Roboto", Arial, sans-serif;
  }
  .sheet {
    width: 1200px; height: 800px;
    display: flex; flex-direction: column;
    align-items: center; justify-content: center; gap: 40px;
  }
  .card {
    position: relative;
    width: 600px; height: 343px;
    box-shadow: 0 2px 6px rgba(0,0,0,0.12);
    overflow: hidden;
  }
  .card--dark { background: var(--charcoal); }
  .card--light { background: var(--paper); }
  .block { position: absolute; background: var(--teal); }
  .block--logo { left: 262px; top: 40px; width: 150px; height: 140px;
    display: flex; align-items: center; justify-content: center; }
  .block--accent { left: 432px; top: 40px; width: 140px; height: 140px; }
  .block--contact { left: 48px; top: 200px; width: 264px; height: 118px; }
  .brand-name {
    font-family: "Roboto", Arial, sans-serif;
    font-weight: 500; font-size: 26px; letter-spacing: 1px;
    color: var(--white);
  }
  .holder { position: absolute; left: 52px; top: 128px; }
  .holder__name {
    font-family: "Roboto Condensed", "Arial Narrow", sans-serif;
    font-weight: 700; font-size: 24px; color: var(--teal);
    text-transform: uppercase; line-height: 1;
  }
  .holder__title { font-size: 14px; margin-top: 4px; line-height: 1; }
  .card--dark .holder__title { color: #e4e4e4; }
  .card--light .holder__title { color: var(--ink); }
  .contact-list {
    position: absolute; left: 20px; bottom: 16px;
    list-style: none; color: var(--white); font-size: 13px;
  }
  .contact-list li { display: flex; align-items: center; gap: 8px; line-height: 17px; }
  .contact-list svg { width: 11px; height: 11px; flex: none; }
</style>
</head>
<body>
<main class="sheet">

  <section class="card card--dark" aria-label="Business card, dark side">
    <div class="block block--logo"><span class="brand-name">PLINDO</span></div>
    <div class="block block--accent"></div>
    <div class="holder">
      <p class="holder__name">Jordan Kessler</p>
      <p class="holder__title">General Manager</p>
    </div>
    <div class="block block--contact">
      <ul class="contact-list">
        <li><svg viewBox="0 0 12 12"><path fill="#fff" d="M2.5 1l2 2-1 1.3c.6 1.4 1.8 2.6 3.2 3.2l1.3-1 2 2-1.3 1.5C5.5 10 2 6.5 1 2.3z"/></svg>555-014-2290</li>
        <li><svg viewBox="0 0 12 12"><rect x="1" y="2.5" width="10" height="7" fill="none" stroke="#fff" stroke-width="1.2"/><path d="M1 2.5l5 4 5-4" fill="none" stroke="#fff" stroke-width="1.2"/></svg>info@plindo.com</li>
        <li><svg viewBox="0 0 12 12"><g fill="none" stroke="#fff" stroke-width="1"><circle cx="6" cy="6" r="5"/><ellipse cx="6" cy="6" rx="2.2" ry="5"/><path d="M1 6h10M2 3.5h8M2 8.5h8"/></g></svg>www.plindo.com</li>
      </ul>
    </div>
  </section>

  <section class="card card--light" aria-label="Business card, light side">
    <div class="block block--logo"><span class="brand-name">PLINDO</span></div>
    <div class="block block--accent"></div>
    <div class="holder">
      <p class="holder__name">Jordan Kessler</p>
      <p class="holder__title">General Manager</p>
    </div>
    <div class="block block--contact">
      <ul class="contact-list">
        <li><svg viewBox="0 0 12 12"><path fill="#fff" d="M2.5 1l2 2-1 1.3c.6 1.4 1.8 2.6 3.2 3.2l1.3-1 2 2-1.3 1.5C5.5 10 2 6.5 1 2.3z"/></svg>555-014-2290</li>
        <li><svg viewBox="0 0 12 12"><rect x="1" y="2.5" width="10" height="7" fill="none" stroke="#fff" stroke-width="1.2"/><path d="M1 2.5l5 4 5-4" fill="none" stroke="#fff" stroke-width="1.2"/></svg>info@plindo.com</li>
        <li><svg viewBox="0 0 12 12"><g fill="none" stroke="#fff" stroke-width="1"><circle cx="6" cy="6" r="5"/><ellipse cx="6" cy="6" rx="2.2" ry="5"/><path d="M1 6h10M2 3.5h8M2 8.5h8"/></g></svg>www.plindo.com</li>
      </ul>
    </div>
  </section>

</main>
</body>
</html>
```